Mix one color into exisiting design, look premium

I have my existing designs, 7 packages. But I want to combine one color inside those designs. I want them to look fit perfectly and look expensive. Premium Products.

You may add anything or change design, make sure to mix the color.

Remember: Your task is to mix the color into my each one of the pakaging designs. Make into new design, look premium for baby products.

```html
<!DOCTYPE html>
<html lang="en">
<head>
<meta charset="utf-8">
<title>Mimi &amp; Bloo Baby Diapers – L</title>
<link href="https://fonts.googleapis.com/css2?family=Lilita+One&family=Poppins:wght@500;600&family=M+PLUS+Rounded+1c:wght@700&display=swap" rel="stylesheet">
<style>
  :root {
    --backdrop: #d6d6d6;
    --sun-yellow: #fccf31;
    --mint: #a6e0d6;
    --mint-light: #b8efe7;
    --royal-navy: #1d2a5c;
    --navy-soft: #2f3f7d;
    --brand-red: #dd2a2e;
    --hole: #bdbdbd;
    --white: #ffffff;
    --art-blue: #7fb0e6;
    --art-coral: #f3a08a;
  }
  * { margin: 0; padding: 0; box-sizing: border-box; }
  html, body { width: 789px; height: 1200px; overflow: hidden; background: var(--backdrop); }
  .stage { position: relative; width: 789px; height: 1200px; }
  .pack { position: absolute; left: 132px; top: 60px; width: 525px; height: 1080px; }
  .brand { font-family: "Lilita One", sans-serif; fill: var(--brand-red); }
  .headline { font-family: "Lilita One", sans-serif; fill: var(--royal-navy); }
  .jp { font-family: "M PLUS Rounded 1c", sans-serif; fill: var(--royal-navy); font-weight: 700; }
  .badge-text { font-family: "Poppins", sans-serif; font-weight: 600; fill: var(--white); letter-spacing: 0.5px; }
  .spec { font-family: "Poppins", sans-serif; font-weight: 500; fill: var(--royal-navy); }
</style>
</head>
<body>
<main class="stage">
  <svg class="pack" viewBox="0 0 523 1035" xmlns="http://www.w3.org/2000/svg">
    <defs>
      <clipPath id="pack-shape"><rect x="0" y="0" width="523" height="1035" rx="12"/></clipPath>
      <linearGradient id="art-tones" x1="0" y1="0" x2="1" y2="1">
        <stop offset="0" stop-color="var(--art-coral)"/>
        <stop offset="0.45" stop-color="var(--art-blue)"/>
        <stop offset="1" stop-color="var(--art-coral)"/>
      </linearGradient>
    </defs>

    <g clip-path="url(#pack-shape)">
      <rect class="pack-body" x="0" y="0" width="523" height="1035" fill="var(--sun-yellow)"/>
      <rect class="seal-strip" x="0" y="0" width="523" height="10" fill="var(--royal-navy)"/>
      <rect class="seal-line" x="0" y="10" width="523" height="2" fill="var(--mint)"/>

      <path class="mint-swoosh" d="M20,100 H523 V180 C515,470 470,800 150,1000 L20,1000 Z" fill="var(--mint)"/>
      <rect class="mint-highlight" x="20" y="100" width="485" height="42" fill="var(--mint-light)"/>
      <ellipse class="sun-disc" cx="150" cy="600" rx="270" ry="330" fill="var(--sun-yellow)"/>

      <rect class="hero-illustration" role="img" aria-label="Cute blue baby elephant with pink ears and a small yellow crown peeking in from the left"
            x="0" y="290" width="330" height="480" rx="40" fill="url(#art-tones)" opacity="0.85"/>

      <rect class="bottom-rule" x="0" y="1025" width="523" height="10" fill="var(--royal-navy)"/>
    </g>

    <text class="brand" x="110" y="54" font-size="17" text-anchor="middle">Mimi &amp; Bloo</text>
    <rect class="hang-hole" x="210" y="28" width="105" height="30" rx="15" fill="var(--hole)"/>
    <text class="headline" x="450" y="45" font-size="13" text-anchor="end">BABY</text>
    <text class="headline" x="450" y="64" font-size="17" text-anchor="end">DIAPERS</text>

    <text class="brand" x="342" y="265" font-size="38" text-anchor="middle">Mimi &amp; Bloo</text>

    <text class="headline" x="228" y="820" font-size="38">BABY</text>
    <text class="jp" x="348" y="802" font-size="14">のおむつ</text>
    <text class="jp" x="348" y="818" font-size="14">赤ちゃん</text>
    <text class="headline" x="228" y="870" font-size="50" textLength="228" lengthAdjust="spacingAndGlyphs">DIAPERS</text>

    <rect class="protection-badge" x="228" y="897" width="228" height="28" rx="6" fill="var(--navy-soft)" stroke="var(--mint)" stroke-width="2"/>
    <text class="badge-text" x="342" y="916" font-size="13" text-anchor="middle">360° HIP PROTECTION</text>

    <rect class="diaper-icon" role="img" aria-label="Small pants-style diaper icon" x="78" y="928" width="38" height="40" rx="9" fill="var(--white)" stroke="#9a9a9a" stroke-width="1"/>
    <text class="spec" x="150" y="962" font-size="13" textLength="306" lengthAdjust="spacingAndGlyphs">L-code  |  9-14kg  |  46PCS  |  UNISEX</text>
  </svg>
</main>
</body>
</html>
```